In need of a Wordpress website for a Water Sports Rental Company!

We are starting a new venture that provides a variety of rental equipment in the Cayman Islands. We are in need of a website where guests are able to book their rental gear during their stay in Cayman. We will also have an interactive map where guests can learn about off the beaten path activities to explore in here Cayman.

Our target market is middle/upper class, so we need a website that appeals to this group. We need our website to be clean, simple and easy to navigate. We need it to be highly visual and modern. We like the idea of the website having a tropical feel to it, we are very open to creative ideas that reflects this!

Must be designed in WordPress using the Lumeria template I’ve provided.

You will find all instructions & the photos I want to use for this website on the following nuvlo account:
- www.nuvlo.example
- Username: hello@tidewrenrentals.example
- Password: marlowe7

All of the photos will need to be resized accordingly to be as small as possible without loosing resolution.

These are the tabs that will be used:
- Home Page
- Adventure Map
- Rental Gear
- Tours
- Photo Gallery
- Contact Us

Home Page
- You will find all the text and instructions for the home page in the word document named ‘Home Page’.

Adventure Map
- You will find all the text and instructions for the home page in the word document named ‘Adventure Map Content’
- There will also be a few 'guide' pages under this tab, which we will go in to detail with the winner.

Rentals
- You will find all the text and instructions for the Rentals page in the word document named ‘Rentals Content’

Tours
- This will just be a page saying ‘kayaking, snorkeling & Bioluminescence tours coming soon’.

Photo Gallery
- You will find the photos for this in our Nuvlo.example Account

Contact Us
- Send us a Message – page will be similar to our other site http://tidewrenrentals.example/contact/
- Phone: +1 (345) 555 0192
- Email: hello@pelicoveouting.example

The big factors on who will have the winning design are:
- The background used
- The layout of the Home Page
- The animations at the top of the Rental Landing Page
- The overall clean, professional look to the website

If you have any questions, don't hesitate to ask.

We look forward to working with you all!!

Good luck!!

Target Market(s)

Middle/Upper Class on vacation with their family

Industry/Entity Type

It Company

Coding

Coded - Design and coding required

Number of Pages Required

5+ page

Colors
fffbf0
cadf82
fbf289
f6faec
fdf9cf
eaf2ce
fff3d1
fee18a
abd037

Requirements
Must have
• - Must be designed in Wordpress using the Lumeria template I have provided or another suitable web template.
• - Must be Responsive Web Design so that the website adjusts to various screen sizes.

```html
<!DOCTYPE html>
<html lang="en">
<head>
<meta charset="utf-8">
<title>Pelicove Outings — Water Sports Rentals</title>
<link href="https://fonts.googleapis.com/css2?family=Open+Sans:wght@400;600;700&family=Patrick+Hand+SC&display=swap" rel="stylesheet">
<style>
:root{
  --green:#abd037;
  --green-dark:#8fb82a;
  --panel:#f6faec;
  --panel-line:#e2ecc8;
  --page:#fbfcf7;
  --text:#555;
  --heading:#9cc431;
  --footer:#333333;
  --footer-bottom:#262626;
  --footer-text:#bdbdbd;
  --white:#ffffff;
}
*{box-sizing:border-box;margin:0;padding:0}
html,body{width:1200px;height:3888px;overflow:hidden}
body{background:var(--page);font-family:"Open Sans",Arial,sans-serif;color:var(--text);font-size:13px;line-height:1.75;position:relative}
.abs{position:absolute}
.hand{font-family:"Patrick Hand SC","Comic Sans MS",cursive;color:var(--heading);font-weight:400}

/* header */
.topbar{left:0;top:0;width:1200px;height:38px;background:var(--green)}
.social{display:flex;gap:8px;left:162px;top:9px}
.social span{width:20px;height:20px;border-radius:50%;border:2px solid var(--white);display:block}
.phone-tab{right:160px;top:0;height:38px;background:#c3df6d;color:var(--white);padding:0 18px;display:flex;align-items:center;gap:8px;font-size:13px}
.brand{left:520px;top:4px;width:160px;height:126px;background:var(--white);border-radius:0 0 80px 80px;display:flex;flex-direction:column;align-items:center;justify-content:center;gap:6px}
.brand .dot{width:34px;height:34px;border-radius:50%;background:var(--green)}
.brand .name{font-family:"Open Sans",sans-serif;font-weight:700;font-size:15px;color:#333;text-align:center;line-height:1.1}
.nav{top:62px;display:flex;gap:30px;font-size:11px;font-weight:600;color:#555;text-transform:uppercase}
.nav.left{left:232px}.nav.right{left:738px}
.nav .active{color:var(--green-dark);border-bottom:2px solid var(--green);border-top:2px solid var(--green);padding:2px 0}
.tagline{top:146px;width:1200px;text-align:center;font-size:34px;letter-spacing:1px}

/* slider */
.slider{left:0;top:202px;width:1200px;height:428px;background:linear-gradient(180deg,#c9d6d8 0%,#9fb0b5 35%,#d9c9ad 60%,#cdb995 100%)}
.play{width:62px;height:62px;border-radius:50%;border:3px solid var(--white)}
.arrow-btn{width:36px;height:36px;border-radius:50%;background:var(--green)}
.dots{display:flex;gap:6px}
.dots span{width:16px;height:5px;background:rgba(255,255,255,.6)}
.dots span.on{background:var(--white)}

/* features */
.feature{top:674px;width:280px;height:207px;background:var(--panel);border:1px solid var(--panel-line)}
.feature .ph{height:140px}
.feature h4{font-size:12px;font-weight:700;color:#444;padding:8px 10px 0;text-transform:uppercase;line-height:1.3}
.feature p{font-size:11px;padding:0 10px;line-height:1.45}
.feature.active{background:var(--green)}
.feature.active h4,.feature.active p{color:var(--white)}

.emblem{width:46px;height:46px;border-radius:50%;background:var(--green)}
.section-title{width:1200px;text-align:center;font-size:36px}

/* welcome */
.video{left:160px;top:1037px;width:428px;height:259px;background:linear-gradient(135deg,#5d7f86,#8ba7a8 55%,#6b8b8c)}
.welcome-text{left:612px;top:1050px;width:428px;font-size:12.5px}

.btn{display:inline-flex;align-items:center;gap:8px;background:var(--green);color:var(--white);font-weight:700;font-size:11px;padding:10px 14px;text-transform:uppercase;letter-spacing:.3px}
.btn i{width:14px;height:14px;border-radius:50%;background:var(--white);position:relative;display:block}
.btn i::after{content:"";position:absolute;left:4px;top:4px;border-left:5px solid var(--green);border-top:3px solid transparent;border-bottom:3px solid transparent}

/* feature rows */
.row-panel{height:236px;background:var(--panel);border:1px solid var(--panel-line)}
.row-img{width:270px;height:180px;box-shadow:0 2px 6px rgba(0,0,0,.15)}
.row-text{width:540px}
.row-text h3{font-family:"Patrick Hand SC",cursive;color:var(--heading);font-weight:400;font-size:22px;line-height:1.2;margin-bottom:8px}
.row-text p{font-size:12px;line-height:1.7;margin-bottom:14px}
.row-text.right{text-align:right}

/* picks */
.pick{top:3276px;width:205px;height:210px;background:var(--panel);border:1px solid var(--panel-line)}
.pick .ph{height:130px}
.pick h5{font-size:11px;font-weight:700;color:#444;padding:7px 8px 0;text-transform:uppercase}
.pick p{font-size:10.5px;line-height:1.4;padding:0 8px}
.pick a{font-size:9px;color:var(--green-dark);font-weight:700;padding:2px 8px;display:block;text-decoration:none}

/* footer */
.footer{left:0;top:3525px;width:1200px;height:285px;background:var(--footer);color:var(--footer-text);font-size:11px}
.footer h6{color:var(--white);font-size:12px;font-weight:700;text-transform:uppercase;margin-bottom:14px}
.footer ul{list-style:none}
.footer li{line-height:2.3}
.footer li::before{content:"›";margin-right:10px;color:var(--green)}
.contact-line{display:flex;gap:14px;margin-bottom:12px;line-height:1.5}
.email-box{display:flex;margin-top:10px}
.email-box span{flex:1;border:1px solid #666;padding:6px 8px;color:#999}
.email-box b{width:30px;border:1px solid #666;border-left:none;color:var(--white);text-align:center;line-height:30px}
.fsocial{display:flex;gap:6px;margin-top:8px}
.fsocial span{width:20px;height:20px;border-radius:50%;border:1px solid #aaa}
.bottombar{left:0;top:3810px;width:1200px;height:78px;background:var(--footer-bottom);color:#999;font-size:10.5px}
</style>
</head>
<body>

<header>
  <div class="abs topbar"></div>
  <div class="abs social"><span></span><span></span><span></span><span></span><span></span><span></span></div>
  <div class="abs phone-tab">
    <svg width="12" height="12" viewBox="0 0 24 24"><path fill="#fff" d="M6.6 10.8a15 15 0 0 0 6.6 6.6l2.2-2.2c.3-.3.7-.4 1-.2 1.1.4 2.3.6 3.6.6.6 0 1 .4 1 1V20c0 .6-.4 1-1 1C10.6 21 3 13.4 3 4c0-.6.4-1 1-1h3.5c.6 0 1 .4 1 1 0 1.3.2 2.5.6 3.6.1.3 0 .7-.2 1z"/></svg>
    +1 (345) 555 0192
  </div>
  <div class="abs brand"><span class="dot"></span><span class="name">Pelicove<br>Outings</span></div>
  <nav class="abs nav left"><span class="active">Home</span><span>Adventure Map</span><span>Rental Gear</span></nav>
  <nav class="abs nav right"><span>Tours</span><span>Photo Gallery</span><span>Contact Us</span></nav>
  <h1 class="abs hand tagline">Cayman's Premier Adventure and Rental Company</h1>
</header>

<section class="abs slider" role="img" aria-label="Blue inflatable kayaks lined up on a sandy beach"></section>
<div class="abs play" style="left:569px;top:385px"></div>
<svg class="abs" style="left:592px;top:403px" width="22" height="26"><polygon points="2,1 20,13 2,25" fill="#fff"/></svg>
<div class="abs arrow-btn" style="left:18px;top:398px"></div>
<svg class="abs" style="left:30px;top:409px" width="12" height="14"><polyline points="9,1 3,7 9,13" fill="none" stroke="#fff" stroke-width="2.5"/></svg>
<div class="abs arrow-btn" style="left:1146px;top:398px"></div>
<svg class="abs" style="left:1158px;top:409px" width="12" height="14"><polyline points="3,1 9,7 3,13" fill="none" stroke="#fff" stroke-width="2.5"/></svg>
<div class="abs dots" style="left:570px;top:598px"><span class="on"></span><span></span><span></span></div>

<section>
  <div class="abs feature" style="left:160px">
    <div class="ph" role="img" aria-label="Two people paddling a kayak in turquoise water" style="background:linear-gradient(180deg,#8fc9dc,#3fa0b8)"></div>
    <h4>Exploration</h4><p>Rent everything you need to get outside and explore the island</p>
  </div>
  <div class="abs feature active" style="left:460px">
    <div class="ph" role="img" aria-label="Calm shallow sea over a reef" style="background:linear-gradient(180deg,#4f9a86,#2f7a6c)"></div>
    <h4>Relaxation</h4><p>We will come straight to your resort or condo and set everything</p>
  </div>
  <div class="abs" style="left:580px;top:728px;width:36px;height:36px;border-radius:50%;background:var(--green)"></div>
  <svg class="abs" style="left:589px;top:737px" width="18" height="18"><circle cx="7" cy="7" r="5" fill="none" stroke="#fff" stroke-width="2"/><line x1="11" y1="11" x2="16" y2="16" stroke="#fff" stroke-width="2"/></svg>
  <div class="abs feature" style="left:760px">
    <div class="ph" role="img" aria-label="Placeholder image for the education feature" style="background:linear-gradient(180deg,#eeeeee,#d8d8d8)"></div>
    <h4>Education</h4><p>We love sharing our knowledge on Cayman's history and the Island's</p>
  </div>
</section>

<section>
  <div class="abs emblem" style="left:577px;top:932px"></div>
  <h2 class="abs hand section-title" style="left:0;top:968px">Welcome to Pelicove Outings!</h2>
  <div class="abs video" role="img" aria-label="Video still of a floating hammock boat on clear water"></div>
  <div class="abs play" style="left:343px;top:1135px;width:58px;height:58px"></div>
  <svg class="abs" style="left:364px;top:1152px" width="22" height="26"><polygon points="2,1 20,13 2,25" fill="#fff"/></svg>
  <div class="abs welcome-text">
    <p>We love having the freedom to explore when travelling and we bet you do to! We are Grand Cayman's premier rental company, offering everything you need to make the most of your vacation. Our website serves as a great starting point to help you prepare for your vacation here in Cayman. We feature a huge selection of adventures on our interactive map with lots of useful information, pictures and directions. Our adventure map is the perfect guide to all our great spots to check out here in Cayman.</p>
    <p style="margin-top:22px"><span class="btn">Know more <i></i></span></p>
  </div>
</section>

<!-- row 1 -->
<div class="abs row-panel" style="left:300px;top:1343px;width:740px"></div>
<div class="abs" style="left:160px;top:1360px;width:280px;height:200px;background:#fff;box-shadow:0 2px 8px rgba(0,0,0,.2)"></div>
<div class="abs" role="img" aria-label="Kayakers on a bright turquoise lagoon" style="left:168px;top:1368px;width:264px;height:184px;background:linear-gradient(180deg,#4dbfc9,#1e9aa9)"></div>
<div class="abs row-text right" style="left:470px;top:1376px;width:550px">
  <h3>Your one stop shop for all the rentals you need here in Cayman!</h3>
  <p>We have a have a huge array of fun toys and equipment for you to enjoy. Whether it's for exploring or relaxing, we have all the equipment you need to make the most of your trip here in Cayman. Need something that we don't stock, just ask and we'll do everything we can to get you the gear you need!</p>
  <span class="btn">Know more <i></i></span>
</div>

<!-- row 2 -->
<div class="abs row-panel" style="left:160px;top:1602px;width:740px"></div>
<div class="abs row-img" role="img" aria-label="Illustrated map of the island" style="left:770px;top:1627px;background:linear-gradient(135deg,#4fc3dd,#7dd3e6 60%,#c7e08a)"></div>
<div class="abs row-text" style="left:180px;top:1630px">
  <h3>Check out our interactive map of Cayman!</h3>
  <p>You won't find any tourist traps on our map! We're all about getting off the beaten path and finding those unique spots and natural wonders to explore. Get our expert advice on which adventures are best for you and how to tackle them!</p>
  <span class="btn">Know more <i></i></span>
</div>

<!-- row 3 -->
<div class="abs row-panel" style="left:300px;top:1861px;width:740px"></div>
<div class="abs row-img" role="img" aria-label="Couple in an inflatable kayak on clear water" style="left:160px;top:1886px;background:linear-gradient(180deg,#9fd6e4,#46a9bf)"></div>
<div class="abs row-text right" style="left:480px;top:1890px">
  <h3>Enjoy complete freedom to explore.</h3>
  <p>Inflatable kayaks have revolutionized the way kayak exploration is done in a way never before. Our kayaks give you the freedom to explore Cayman's most secluded locations and snorkel those hard to reach reefs. Our kayaks are light, comfortable and easy to use.</p>
  <span class="btn">Know more <i></i></span>
</div>

<!-- row 4 -->
<div class="abs row-panel" style="left:160px;top:2120px;width:740px"></div>
<div class="abs row-img" role="img" aria-label="Beach cruiser bikes parked by the sea" style="left:770px;top:2140px;background:linear-gradient(180deg,#8fd0e0,#e3d6b4)"></div>
<div class="abs row-text" style="left:180px;top:2143px">
  <h3>There's no easier way to get around the island.</h3>
  <p>What better way is there to explore the island other than to rent a bike and go! Our mountain bikes are perfect for those interested on heading out on a full day adventure. If you're looking for something more casual, renting a cruiser is perfect to get around the Seven Mile Beach area. Use our map to help guide you to all our suggested locations to explore!</p>
  <span class="btn">Know more <i></i></span>
</div>

<!-- row 5 -->
<div class="abs row-panel" style="left:300px;top:2364px;width:740px"></div>
<div class="abs row-img" role="img" aria-label="Placeholder image for concierge service" style="left:160px;top:2390px;background:linear-gradient(180deg,#f5f5f5,#e2e2e2)"></div>
<div class="abs row-text right" style="left:480px;top:2380px">
  <h3>We want to be your personal concierge and help you to plan out your trip!</h3>
  <p>When we come to deliver your equipment, we teach you everything you need to know about the island including the best hidden spots, best restaurants &amp; bars to eat &amp; drink and anything else you might be curious about. Please don't hesitate to contact us for any and all of your vacation questions. We are happy to help!</p>
  <span class="btn">Know more <i></i></span>
</div>

<!-- row 6 -->
<div class="abs row-panel" style="left:160px;top:2623px;width:740px"></div>
<div class="abs row-img" role="img" aria-label="Family relaxing on a floating hammock boat" style="left:770px;top:2648px;background:linear-gradient(180deg,#3fb3bf,#1d8e9d)"></div>
<div class="abs row-text" style="left:180px;top:2650px">
  <h3>Is it a boat? Is it a whale?.... It's a Driftnest!</h3>
  <p>Easily one of the coolest inventions we've ever come across, the Driftnest is a versatile toy the whole family can enjoy together. Spend the day cruising along Seven Mile Beach in style as you bar hop with your clan. Better still, bring a cooler on board and put the kids to work paddling as you relax in your hammock on the crystal clear waters!</p>
  <span class="btn">Know more <i></i></span>
</div>

<!-- row 7 -->
<div class="abs row-panel" style="left:300px;top:2877px;width:740px"></div>
<div class="abs row-img" role="img" aria-label="Snorkeler swimming underwater in a full face mask" style="left:160px;top:2905px;background:linear-gradient(180deg,#5fc4db,#1c7fa3)"></div>
<div class="abs row-text right" style="left:480px;top:2915px">
  <h3>A new way to snorkel!</h3>
  <p>Our full face snorkel masks are easy to use, making them perfect for kids and beginners. You simply put the mask on and breath as you usually would. There's no need to get used to breathing from your mouth and you don't experience a sore jaw from having to hold the mouth piece in place. Just ask and we'll bring one along for you to try!</p>
  <span class="btn">Know more <i></i></span>
</div>

<section>
  <div class="abs emblem" style="left:577px;top:3160px"></div>
  <h2 class="abs hand section-title" style="left:0;top:3202px">Our Adventure Top-Picks</h2>
  <div class="abs pick" style="left:160px"><div class="ph" role="img" aria-label="Glowing blue bioluminescent bay at night" style="background:linear-gradient(180deg,#0b1d3a,#1f5fa8)"></div><h5>Bio Bay</h5><p>Lorem ipsum dolor sit amet, pics consectetur adipiscing elit.</p><a>READ MORE →</a></div>
  <div class="abs pick" style="left:385px"><div class="ph" role="img" aria-label="Sunken ship wreck under blue water" style="background:linear-gradient(180deg,#2aa3c4,#115f7e)"></div><h5>Kittiwake</h5><p>Lorem ipsum dolor sit amet, pics consectetur adipiscing elit.</p><a>READ MORE →</a></div>
  <div class="abs pick" style="left:610px"><div class="ph" role="img" aria-label="Small sandy cay surrounded by turquoise sea" style="background:linear-gradient(180deg,#7cc9dd,#3fa9c0 55%,#e7dcc0)"></div><h5>Sand Cay Island</h5><p>Lorem ipsum dolor sit amet, pics consectetur adipiscing elit.</p><a>READ MORE →</a></div>
  <div class="abs pick" style="left:835px"><div class="ph" role="img" aria-label="Stingrays gliding over a sandbar" style="background:linear-gradient(180deg,#3cb6c3,#2a8a98)"></div><h5>Stingray City</h5><p>Lorem ipsum dolor sit amet, pics consectetur adipiscing elit.</p><a>READ MORE →</a></div>
</section>

<footer class="abs footer">
  <div class="abs" style="left:160px;top:30px;width:200px">
    <div style="display:flex;align-items:center;gap:10px;margin-bottom:18px"><span style="width:40px;height:40px;border-radius:50%;background:var(--green);display:block"></span><span style="font-weight:700;font-size:15px;color:#fff">Pelicove Outings</span></div>
    <p style="line-height:1.6">We love having the freedom to explore when travelling and we bet you do to! We are Grand Cayman's premier rental company, offering everything you need to make the most of your vacation.</p>
  </div>
  <div class="abs" style="left:385px;top:30px">
    <h6>Quick Links</h6>
    <ul><li>Home</li><li>Adventure Map</li><li>Rental Gear</li><li>Tours</li><li>Photo Gallery</li><li>Contact Us</li></ul>
  </div>
  <div class="abs" style="left:610px;top:30px;width:200px">
    <h6>Get in Touch</h6>
    <div class="contact-line"><svg width="12" height="16" viewBox="0 0 12 16"><path d="M6 0a6 6 0 0 0-6 6c0 4.5 6 10 6 10s6-5.5 6-10a6 6 0 0 0-6-6zm0 8.5A2.5 2.5 0 1 1 6 3.5a2.5 2.5 0 0 1 0 5z" fill="#ccc"/></svg><span>48 Harbour Lane, West Bay,<br>Grand Cayman,<br>Box 100 KY1-0000 Cayman Islands</span></div>
    <div class="contact-line"><svg width="12" height="12" viewBox="0 0 24 24"><path fill="#ccc" d="M6.6 10.8a15 15 0 0 0 6.6 6.6l2.2-2.2c.3-.3.7-.4 1-.2 1.1.4 2.3.6 3.6.6.6 0 1 .4 1 1V20c0 .6-.4 1-1 1C10.6 21 3 13.4 3 4c0-.6.4-1 1-1h3.5c.6 0 1 .4 1 1 0 1.3.2 2.5.6 3.6.1.3 0 .7-.2 1z"/></svg><span>+1 (345) 555 0192</span></div>
    <div class="contact-line"><svg width="14" height="10" viewBox="0 0 14 10"><rect x="0.5" y="0.5" width="13" height="9" fill="none" stroke="#ccc"/><polyline points="0.5,0.5 7,5.5 13.5,0.5" fill="none" stroke="#ccc"/></svg><span>hello@pelicoveouting.example</span></div>
  </div>
  <div class="abs" style="left:835px;top:30px;width:205px">
    <h6>Newsletter</h6>
    <p style="line-height:1.5">Do you want to receive our marketing campaigns to get more value from them?</p>
    <div class="email-box"><span>Enter your email address</span><b>+</b></div>
    <h6 style="margin-top:18px;margin-bottom:4px">Follow Us On</h6>
    <div class="fsocial"><span></span><span></span><span></span><span></span><span></span><span></span></div>
  </div>
</footer>
<div class="abs bottombar">
  <span class="abs" style="left:160px;top:31px">© 2017 pelicoveouting.example. All right reserved</span>
  <span class="abs" style="left:885px;top:31px">Privacy Policy &nbsp;&nbsp;|&nbsp;&nbsp; Terms of Use</span>
</div>

</body>
</html>
```